Business card for a doctor's practice

Would like a business card for a Pulmonary ( lung) doctor. I would like to include a logo with something in reference to air or oxygen or lungs. Would like the color red included somehow. Name of the company is Breathwell Medical Associates of Eastern Ridgeford and we specialize in Pulmonary Medicine,. I would like something streamlined and modern
Target Market(s)
Patients, hospitals, other doctors
Industry/Entity Type
Business
Contact Information for Business Card
Would like business details superimposed on a logo somehow

```html
<!DOCTYPE html>
<html lang="en">
<head>
<meta charset="utf-8">
<title>Breathwell Medical Associates – Business Card</title>
<link href="https://fonts.googleapis.com/css2?family=Figtree:wght@400;500&family=Open+Sans:wght@400;700&display=swap" rel="stylesheet">
<style>
  :root {
    --brand-red: #e21f27;
    --ring-red: #e0262d;
    --ink-grey: #555558;
    --paper: #ffffff;
    --backdrop: #dcdcdf;
  }
  * { box-sizing: border-box; margin: 0; padding: 0; }
  html, body { width: 994px; height: 1200px; overflow: hidden; }
  body { background: var(--backdrop); position: relative; font-family: "Open Sans", sans-serif; }

  .brand-panel {
    position: absolute; left: 0; top: 0; width: 994px; height: 369px;
    background: var(--paper);
  }
  .brand-ring {
    position: absolute; border: 3px solid var(--ring-red); border-radius: 50%;
  }
  .brand-name {
    position: absolute; left: 0; width: 100%; text-align: center;
    font-family: "Figtree", sans-serif; font-weight: 500; color: var(--brand-red);
    line-height: 1;
  }
  .brand-name .line-two { display: block; letter-spacing: 0.16em; }

  .panel-ring { left: 429px; top: 66px; width: 136px; height: 136px; }
  .panel-name { top: 222px; font-size: 44px; }
  .panel-name .line-two { font-size: 28px; margin-top: 10px; }

  .card {
    position: absolute; left: 221px; width: 552px; height: 329px;
    background: var(--paper); border-radius: 18px; overflow: hidden;
  }
  .card-front { top: 431px; }
  .card-back { top: 811px; }

  .front-ring { left: 235px; top: 28px; width: 82px; height: 82px; border-width: 2px; }
  .front-name { top: 120px; font-size: 29px; }
  .front-name .line-two { font-size: 19px; margin-top: 6px; }

  .contact-band {
    position: absolute; left: 0; top: 193px; width: 100%; height: 110px;
    background: var(--brand-red); color: var(--paper);
  }
  .holder {
    position: absolute; right: 297px; top: 18px; text-align: right;
    font-size: 13px; line-height: 1.3;
  }
  .holder-name { font-weight: 700; font-size: 16px; letter-spacing: 0.01em; }
  .holder-role { margin-bottom: 10px; }
  .contact-list {
    position: absolute; left: 284px; top: 19px; list-style: none;
    font-size: 13px; line-height: 20px;
  }
  .contact-list li { display: flex; align-items: center; gap: 6px; }
  .contact-list svg { width: 12px; height: 12px; fill: var(--paper); flex: none; }

  .back-ring { left: 229px; top: 82px; width: 94px; height: 94px; }
  .back-name { top: 189px; font-size: 33px; }
  .back-name .line-two { font-size: 21px; margin-top: 7px; }
</style>
</head>
<body>

<section class="brand-panel">
  <div class="brand-ring panel-ring"></div>
  <h1 class="brand-name panel-name">BREATHWELL MEDICAL<span class="line-two">ASSOCIATES</span></h1>
</section>

<article class="card card-front">
  <div class="brand-ring front-ring"></div>
  <h2 class="brand-name front-name">BREATHWELL MEDICAL<span class="line-two">ASSOCIATES</span></h2>

  <div class="contact-band">
    <div class="holder">
      <p class="holder-name">ADRIAN MERCER</p>
      <p class="holder-role">President</p>
      <p>418 Harbor Lane,</p>
      <p>Ridgeford, NY 11720</p>
    </div>
    <ul class="contact-list">
      <li><svg viewBox="0 0 12 12"><path d="M3 0h6v12H3zM4 1.5v6h4v-6zM5 9h2v1.5H5z" fill-rule="evenodd"/></svg>+ 000 000 000</li>
      <li><svg viewBox="0 0 12 12"><path d="M0 4c2-3 10-3 12 0l-2 1.5-1.5-1.5h-5L2 5.5zM3 6h6l2 5H1z"/></svg>+ 000 000 000</li>
      <li><svg viewBox="0 0 12 12"><path d="M0 2h12v8H0zM1 3l5 4 5-4v-.2H1z" fill-rule="evenodd"/></svg>info@breathwellmed.com</li>
      <li><svg viewBox="0 0 12 12"><path d="M6 0a6 6 0 1 0 0 12A6 6 0 0 0 6 0zm0 1.5a4.5 4.5 0 1 1 0 9 4.5 4.5 0 0 1 0-9zM5 4l4 2-4 2z" fill-rule="evenodd"/></svg>www.breathwellmed.com</li>
    </ul>
  </div>
</article>

<article class="card card-back">
  <div class="brand-ring back-ring"></div>
  <h2 class="brand-name back-name">BREATHWELL MEDICAL<span class="line-two">ASSOCIATES</span></h2>
</article>

</body>
</html>
```